Kemo Logistics App for American company. Will be like Zolva freight but more grassroots

We need a logistics App, similar to a truck broker. Similar to the Zolva or Brakk apps where a truck driver can connect with companies and pick up the freight to get paid. The company is called KEMO after the Morroxan explorer Ravi Domenek. Zolva freight has an app can be similar but more driver focused.

Target Market(s)

Everyone who needs freight moved from one place to next

Industry/Entity Type

Trucking

Requirements
Must have
• GPS and easy to use interface between driver and companies
Nice to have
• Colors that are travel like and friendly
Should not have
• Be boring or plain or hard to understand

```html
<!DOCTYPE html>
<html lang="en">
<head>
<meta charset="utf-8">
<title>Kemo Logistics – App Screens</title>
<link rel="stylesheet" href="https://fonts.googleapis.com/css2?family=Quicksand:wght@700&family=Roboto:wght@400;500;700&display=swap">
<style>
  :root{
    --brand:#1f2bf0;
    --brand-soft:#3a45ff;
    --ink:#15161a;
    --muted:#8b8e99;
    --line:#e3e5ec;
    --surface:#ffffff;
    --screen-bg:#f2f3f7;
    --stage:#050507;
    --band:#2a33e8;
    --overlay:#5d6068;
  }
  *{box-sizing:border-box;margin:0;padding:0}
  html,body{width:956px;height:1200px;overflow:hidden}
  body{background:var(--stage);font-family:"Roboto",sans-serif;color:var(--ink);position:relative}
  .band{position:absolute;left:0;top:0;width:956px;height:420px}
  .screen{position:absolute;width:208px;height:450px;border-radius:26px;overflow:hidden;background:var(--screen-bg)}
  .s-welcome{left:82px;top:100px;background:var(--surface)}
  .s-book{left:374px;top:100px}
  .s-details{left:666px;top:100px}
  .s-booked{left:228px;top:640px;background:var(--overlay)}
  .s-driver{left:520px;top:640px}
  .abs{position:absolute}

  .appbar{position:absolute;left:0;top:0;width:100%;height:55px;background:var(--surface)}
  .status{position:absolute;top:10px;left:12px;right:12px;display:flex;justify-content:space-between;font-size:7px;font-weight:500}
  .appbar .back{position:absolute;left:12px;top:29px}
  .appbar .title{position:absolute;left:0;right:0;top:26px;text-align:center;font-size:11.5px;font-weight:500}
  .menu{position:absolute;right:10px;top:26px;width:19px;height:19px;border-radius:50%;background:#e6e7ec;display:flex;align-items:center;justify-content:center}

  /* welcome */
  .hero{position:absolute;left:0;top:0;width:100%;height:248px;background:linear-gradient(180deg,#5b6478 0%,#c48a3e 28%,#7a8088 55%,#9aa0a6 78%,#ffffff 100%)}
  .brand-name{position:absolute;left:12px;top:263px;font-size:10px;font-weight:500;color:#6d707a}
  .headline{position:absolute;left:12px;top:283px;width:190px;font-family:"Quicksand",sans-serif;font-weight:700;font-size:16.5px;line-height:17px;color:#111}
  .btn{position:absolute;background:var(--brand);color:#fff;font-weight:500;display:flex;align-items:center;justify-content:center;border-radius:14px;box-shadow:0 6px 10px rgba(31,43,240,.3)}
  .tour{position:absolute;left:0;right:0;top:411px;text-align:center;font-size:10px;font-weight:500}

  /* calendar */
  .calendar{position:absolute;left:13px;top:75px;width:182px;height:90px;background:var(--surface);border-radius:5px;overflow:hidden}
  .cal-head{height:27px;background:var(--brand);color:#fff;font-size:10px;font-weight:500;display:flex;align-items:center;justify-content:center;position:relative}
  .cal-nav{position:absolute;top:6px;width:15px;height:15px;border-radius:50%;background:#fff;display:flex;align-items:center;justify-content:center}
  .cal-row{display:flex;justify-content:space-around;padding:0 6px}
  .cal-days{font-size:6px;color:#666;margin-top:11px;padding-bottom:7px;border-bottom:1px dotted #ccc;margin-left:8px;margin-right:8px}
  .cal-dates{font-size:7.5px;color:#999;margin-top:8px}
  .cal-dates span{width:16px;height:16px;display:flex;align-items:center;justify-content:center}
  .cal-dates .on{background:var(--brand);color:#fff;border-radius:50%}
  .cal-dates .cur{color:#222}
  .search{position:absolute;left:12px;top:188px;width:184px;height:27px;background:var(--surface);border-radius:14px;font-size:8.5px;display:flex;align-items:center}
  .search small{font-size:5.5px;color:#888;margin:0 3px 0 44px}
  .list-head{position:absolute;left:12px;right:11px;top:232px;display:flex;justify-content:space-between;align-items:baseline;font-size:10px}
  .list-head .sort{font-size:8px;color:var(--brand)}

  /* load block */
  .load{position:absolute;left:10px;width:190px}
  .dh{font-size:8px;color:var(--muted);word-spacing:6px}
  .stop{display:flex;justify-content:space-between;font-size:8px;margin-left:12px;margin-right:4px}
  .stop time{font-size:5.5px;color:#aaa}
  .route-dot{position:absolute;left:4px;width:6px;height:6px}
  .route-line{position:absolute;left:6.5px;width:1px;border-left:1.3px dotted #333}
  .divider{position:absolute;left:2px;right:0;height:1px;background:var(--line)}
  .truck{position:absolute;width:46px;height:26px;border-radius:3px;background:linear-gradient(90deg,#2b3f9e 0 32%,#e4e6ea 32%)}
  .pick{position:absolute;font-size:10px}
  .pick .sub{font-size:7.5px;color:var(--muted);margin-top:2px}
  .pick .hrs{font-size:7px;color:var(--brand);margin-top:5px}
  .price{position:absolute;text-align:right;font-size:9px;color:var(--brand);font-weight:500}
  .price small{display:block;font-size:6.5px;color:#666;font-weight:400;margin-top:2px}
  .heart{position:absolute;width:17px;height:17px;border-radius:50%;background:#c9cbd1;display:flex;align-items:center;justify-content:center}
  .hint{position:absolute;left:0;right:0;top:415px;text-align:center;font-size:8px;color:#777}

  /* details */
  .map{position:absolute;left:0;top:55px;width:100%;height:215px;background:linear-gradient(135deg,#e9eaee,#d9dbe0 60%,#e4e5e9)}
  .sheet{position:absolute;left:2px;right:2px;top:258px;bottom:0;background:var(--surface);border-radius:16px 16px 0 0}

  /* booked */
  .dim{position:absolute;inset:0;background:linear-gradient(180deg,#4f5259,#6a6d74)}
  .modal{position:absolute;left:8px;right:8px;top:218px;height:180px;background:var(--surface);border-radius:4px;text-align:center}
  .modal h2{position:absolute;left:0;right:0;top:82px;font-size:9.5px;font-weight:500}
  .modal p{position:absolute;left:0;right:0;top:102px;font-size:7.5px;color:#777;line-height:11px}
  .dismiss{position:absolute;left:8px;right:8px;top:405px;height:33px;background:var(--surface);border-radius:4px;font-size:9px;display:flex;align-items:center;justify-content:center}

  /* drivers */
  .group{position:absolute;left:12px;font-size:9.5px;font-weight:500}
  .driver{position:absolute;left:11px;width:186px;height:55px;background:var(--surface);border-radius:3px}
  .avatar{position:absolute;left:5px;top:7px;width:41px;height:41px;border-radius:50%;background:linear-gradient(160deg,#c9b8a6,#5b4c40)}
  .driver .name{position:absolute;left:54px;top:9px;font-size:9.5px;font-weight:500}
  .meta{position:absolute;top:29px;font-size:6px;color:#888}
  .meta b{display:block;font-size:7.5px;color:#111;font-weight:500;margin-top:3px}
</style>
</head>
<body>

<svg class="band" viewBox="0 0 956 420" aria-hidden="true">
  <path d="M0 0H956V315Q478 420 0 315Z" fill="var(--band)"/>
</svg>

<!-- Welcome -->
<section class="screen s-welcome">
  <div class="hero" role="img" aria-label="Photo of a truck on a highway at sunset"></div>
  <div class="brand-name">Kemo Logistics</div>
  <h1 class="headline">Freedom to haul the way you want</h1>
  <div class="btn" style="left:47px;top:341px;width:115px;height:25px;font-size:8.5px">BOOK NOW</div>
  <div class="tour">Take tour to Kemo Logistics</div>
</section>

<!-- Book -->
<section class="screen s-book">
  <header class="appbar">
    <div class="status"><span>12:00 ➚</span><span>▮▮▮ ◔ ▬</span></div>
    <svg class="back" width="12" height="7" viewBox="0 0 12 7"><path d="M12 3.5H1M3.5 1 1 3.5 3.5 6" stroke="#111" stroke-width="1.4" fill="none"/></svg>
    <div class="title">Book</div>
    <div class="menu"><svg width="8" height="7"><path d="M0 1H8M0 3.5H8M0 6H8" stroke="#111" stroke-width="1.2"/></svg></div>
  </header>
  <div class="calendar">
    <div class="cal-head">
      <span class="cal-nav" style="left:9px"><svg width="5" height="7"><path d="M4 1 1 3.5 4 6" stroke="#111" fill="none" stroke-width="1.2"/></svg></span>
      May 2021
      <span class="cal-nav" style="right:9px"><svg width="5" height="7"><path d="M1 1 4 3.5 1 6" stroke="#111" fill="none" stroke-width="1.2"/></svg></span>
    </div>
    <div class="cal-row cal-days"><span>SUN</span><span>MON</span><span>TUE</span><span>WED</span><span>THU</span><span>FRI</span><span>SAT</span></div>
    <div class="cal-row cal-dates"><span>28</span><span>29</span><span>30</span><span>31</span><span class="on">1</span><span class="cur">2</span><span class="cur">3</span></div>
  </div>
  <div class="search">
    <svg style="margin-left:9px" width="9" height="9"><circle cx="3.6" cy="3.6" r="2.8" stroke="#111" stroke-width="1.3" fill="none"/><path d="M5.7 5.7 8.5 8.5" stroke="#111" stroke-width="1.4"/></svg>
    <small>ALL LOADS:</small>Near You
  </div>
  <div class="list-head"><span>Today</span><span class="sort">Sort: Deadhead</span></div>
  <div class="load" style="top:270px;height:140px">
    <div class="dh">6mins deadhead</div>
    <span class="route-dot" style="top:17px;border-radius:50%;background:var(--brand)"></span>
    <span class="route-line" style="top:24px;height:14px"></span>
    <span class="route-dot" style="top:40px;background:#111"></span>
    <div class="stop" style="margin-top:8px"><span>512 Marrow Crossing</span><time>7:15 PM</time></div>
    <div class="stop" style="margin-top:14px"><span>40 Quillan Square</span><time>9:30 PM</time></div>
    <span class="divider" style="top:62px"></span>
    <div class="truck" style="left:2px;top:80px" role="img" aria-label="Truck photo"></div>
    <div class="pick" style="left:62px;top:80px">Pickup<div class="sub">Today, 08:30 AM</div><div class="hrs">08:00am - 09:00 pm</div></div>
    <div class="price" style="right:4px;top:80px">$480<small>Per Day</small></div>
    <div class="heart" style="right:5px;top:112px"><svg width="9" height="8"><path d="M4.5 7.5 1 4A2 2 0 0 1 4.5 1.5 2 2 0 0 1 8 4Z" stroke="#fff" fill="none"/></svg></div>
  </div>
  <div class="hint" style="top:405px">Like loads you've previously hauled</div>
</section>

<!-- Load details -->
<section class="screen s-details">
  <header class="appbar">
    <div class="status"><span>12:00 ➚</span><span>▮▮▮ ◔ ▬</span></div>
    <svg class="back" width="12" height="7" viewBox="0 0 12 7"><path d="M12 3.5H1M3.5 1 1 3.5 3.5 6" stroke="#111" stroke-width="1.4" fill="none"/></svg>
    <div class="title">Load Details</div>
    <div class="menu"><svg width="8" height="7"><path d="M0 1H8M0 3.5H8M0 6H8" stroke="#111" stroke-width="1.2"/></svg></div>
  </header>
  <div class="map" role="img" aria-label="Street map with truck positions near the pickup point"></div>
  <div class="sheet">
    <div class="load" style="left:8px;top:14px;height:130px">
      <div class="dh">6mins deadhead</div>
      <span class="route-dot" style="top:17px;border-radius:50%;background:var(--brand)"></span>
      <span class="route-line" style="top:24px;height:14px"></span>
      <span class="route-dot" style="top:40px;background:#111"></span>
      <div class="stop" style="margin-top:8px"><span>512 Marrow Crossing</span><time>7:15 PM</time></div>
      <div class="stop" style="margin-top:14px"><span>40 Quillan Square</span><time>9:30 PM</time></div>
      <span class="divider" style="top:62px"></span>
      <div class="truck" style="left:2px;top:80px" role="img" aria-label="Truck photo"></div>
      <div class="pick" style="left:62px;top:80px">Pickup<div class="sub">Today, 08:30 AM</div><div class="hrs">08:00am - 09:00 pm</div></div>
      <div class="price" style="right:4px;top:80px">$480<small>Per Day</small></div>
      <div class="heart" style="right:5px;top:112px"><svg width="9" height="8"><path d="M4.5 7.5 1 4A2 2 0 0 1 4.5 1.5 2 2 0 0 1 8 4Z" stroke="#fff" fill="none"/></svg></div>
    </div>
  </div>
  <div class="btn" style="left:29px;top:411px;width:150px;height:29px;font-size:9px">BOOK LOAD</div>
</section>

<!-- Load booked -->
<section class="screen s-booked">
  <div class="dim" role="img" aria-label="Dimmed load details map behind the dialog"></div>
  <div class="modal">
    <svg class="abs" style="left:72px;top:20px" width="46" height="46" viewBox="0 0 46 46" fill="none" stroke="var(--brand)" stroke-width="2.4" stroke-linejoin="round">
      <rect x="3" y="22" width="8" height="20"/>
      <path d="M11 24 19 14V5a4 4 0 0 1 4 4v9h13a3 3 0 0 1 0 6h-2a3 3 0 0 1 0 6h-2a3 3 0 0 1 0 6h-3a3 3 0 0 1 0 6H11"/>
      <path d="M22 1V-2M30 4l3-3M16 4 13 1" stroke-linecap="round"/>
    </svg>
    <h2>LOAD BOOKED</h2>
    <p>You're dropping off in Grand Prarie, TX.<br>Do you also want to see reloads?</p>
    <div class="btn" style="left:9px;right:9px;top:148px;height:24px;font-size:8.5px;border-radius:3px;box-shadow:none">VIEW 2 RELOADS</div>
  </div>
  <div class="dismiss">Dismiss</div>
</section>

<!-- Assign a driver -->
<section class="screen s-driver">
  <header class="appbar">
    <div class="status"><span>12:00 ➚</span><span>▮▮▮ ◔ ▬</span></div>
    <svg class="back" width="12" height="7" viewBox="0 0 12 7"><path d="M12 3.5H1M3.5 1 1 3.5 3.5 6" stroke="#111" stroke-width="1.4" fill="none"/></svg>
    <div class="title">Assign a Driver</div>
    <div class="menu"><svg width="8" height="7"><path d="M0 1H8M0 3.5H8M0 6H8" stroke="#111" stroke-width="1.2"/></svg></div>
  </header>
  <div class="group" style="top:80px">Available</div>
  <div class="driver" style="top:97px"><div class="avatar" role="img" aria-label="Driver portrait"></div><div class="name">Owen Hartley</div><div class="meta" style="left:54px">Current Location<b>Houston, TX</b></div><div class="meta" style="left:121px">Deadhead<b>3min</b></div></div>
  <div class="driver" style="top:165px"><div class="avatar" role="img" aria-label="Driver portrait"></div><div class="name">Owen Hartley</div><div class="meta" style="left:54px">Current Location<b>Houston, TX</b></div><div class="meta" style="left:121px">Deadhead<b>3min</b></div></div>
  <div class="driver" style="top:232px"><div class="avatar" role="img" aria-label="Driver portrait"></div><div class="name">Owen Hartley</div><div class="meta" style="left:54px">Current Location<b>Houston, TX</b></div><div class="meta" style="left:121px">Deadhead<b>3min</b></div></div>
  <div class="group" style="top:318px">Unavailable</div>
  <div class="driver" style="top:335px"><div class="avatar" role="img" aria-label="Driver portrait"></div><div class="name">Owen Hartley</div><div class="meta" style="left:54px">Current Location<b>Houston, TX</b></div><div class="meta" style="left:121px">Deadhead<b>3min</b></div></div>
  <div class="btn" style="left:29px;top:410px;width:150px;height:29px;font-size:9px">SELECT DRIVER</div>
</section>

</body>
</html>
```